Marlowe Finch Cocktail Menu design

I need a new cocktail menu for our bar 'Marlowe Finch'.

The logo should read just the full Marlowe Finch text logo at the top, and the small 'MF' part of the logo in the bottom corners.

The design should be slick, and modern to fit in with our club/bar branding which can be viewed on our social media or website www.marlowefinch.co.uk

```html
<!DOCTYPE html>
<html lang="en">
<head>
<meta charset="utf-8">
<title>MF's Long List of Long Islands – Marlowe Finch</title>
<link rel="stylesheet" href="https://fonts.googleapis.com/css2?family=Oswald:wght@500;600;700&display=swap">
<style>
  :root {
    --ink: #ffffff;
    --ground: #0b0c0b;
    --ground-soft: #161815;
    --label-ink: #000000;
  }
  * { margin: 0; padding: 0; box-sizing: border-box; }
  html, body {
    width: 848px; height: 1200px; overflow: hidden;
    background: var(--ground);
  }
  .menu {
    position: relative; width: 848px; height: 1200px; overflow: hidden;
    background: var(--ground);
    color: var(--ink);
    font-family: "Oswald", "Arial Narrow", sans-serif;
  }
  .menu__photo {
    position: absolute; inset: 0;
    background:
      radial-gradient(ellipse 160px 300px at 420px 560px, rgba(106,74,18,0.55), transparent 75%),
      radial-gradient(ellipse 120px 90px at 660px 200px, rgba(122,58,16,0.6), transparent 75%),
      radial-gradient(ellipse 140px 160px at 740px 760px, rgba(106,74,18,0.45), transparent 75%),
      radial-gradient(ellipse 200px 120px at 150px 720px, rgba(44,74,28,0.45), transparent 75%),
      radial-gradient(ellipse 90px 110px at 800px 1130px, rgba(44,74,28,0.6), transparent 75%),
      radial-gradient(ellipse 360px 500px at 430px 600px, rgba(44,74,28,0.35), transparent 80%),
      linear-gradient(180deg, var(--ground) 0%, var(--ground-soft) 50%, var(--ground) 100%);
  }
  .brand {
    position: absolute; top: 150px; left: 0; width: 100%;
    text-align: center;
  }
  .brand__name {
    font-weight: 700; font-size: 52px; line-height: 1;
    letter-spacing: 1px; text-transform: uppercase;
  }
  .brand__tagline {
    margin-top: 14px;
    font-weight: 600; font-size: 12px; letter-spacing: 4px;
  }
  .title {
    position: absolute; top: 272px; left: 78px; width: 692px;
    display: flex; align-items: center; justify-content: space-between;
    font-weight: 700; font-size: 48px; line-height: 1;
    letter-spacing: 0.2px; white-space: nowrap;
  }
  .title__label {
    height: 66px; padding: 0 14px;
    display: flex; align-items: center;
    background: var(--ink); color: var(--label-ink);
  }
  .drinks {
    position: absolute; top: 406px; left: 67px; width: 723px;
    list-style: none;
  }
  .drink { height: 92px; }
  .drink__head {
    display: flex; align-items: center; height: 36px;
  }
  .drink__name {
    font-weight: 700; font-size: 26px; text-transform: uppercase; line-height: 1;
    white-space: nowrap;
  }
  .drink__rule {
    flex: 1; height: 1px; background: var(--ink);
    margin: 0 9px 0 8px;
  }
  .drink__price {
    flex: none; white-space: nowrap; text-align: right;
    font-weight: 700; font-size: 25px; line-height: 1;
    position: relative; top: -5px;
  }
  .drink__mix {
    font-weight: 600; font-size: 19px; line-height: 1; margin-top: 2px;
    white-space: nowrap;
  }
  .offer {
    position: absolute; top: 994px; left: 0; width: 100%;
    text-align: center;
    font-weight: 700; font-size: 50px; line-height: 61px;
    text-transform: uppercase;
  }
  .footer-mark {
    position: absolute; left: 26px; top: 1106px;
    font-weight: 700; font-size: 64px; line-height: 1;
  }
  .footer-rule {
    position: absolute; left: 132px; top: 1155px;
    width: 625px; height: 1px; background: var(--ink);
  }
</style>
</head>
<body>
<main class="menu">
  <div class="menu__photo" role="img" aria-label="Dark moody photograph of a tall cocktail glass with a red straw, orange slice, mint leaves, kiwi and fruit scattered on a black slate surface"></div>

  <header class="brand">
    <div class="brand__name">Marlowe Finch</div>
    <div class="brand__tagline">BAR . CLUB . FOOD</div>
  </header>

  <h1 class="title"><span>MF’s LONG LIST OF</span><span class="title__label">‘LONG ISLANDS’</span></h1>

  <ul class="drinks">
    <li class="drink">
      <div class="drink__head"><span class="drink__name">Long Island Iced Tea</span><span class="drink__rule"></span><span class="drink__price">£ 9.50</span></div>
      <p class="drink__mix">Vodka, Gin, Rum, Tequila, Orange Liqueur, Lemon &amp; Cola</p>
    </li>
    <li class="drink">
      <div class="drink__head"><span class="drink__name">Long Beach Iced Tea</span><span class="drink__rule"></span><span class="drink__price">£ 9.50</span></div>
      <p class="drink__mix">Vodka, Gin, Rum, Tequila, Orange Liqueur, Lemon &amp; Cranberry</p>
    </li>
    <li class="drink">
      <div class="drink__head"><span class="drink__name">AMF</span><span class="drink__rule"></span><span class="drink__price">£ 9.50</span></div>
      <p class="drink__mix">Vodka, Gin, Rum, Tequila, Blue Curacao, Lemon &amp; Lemonade</p>
    </li>
    <li class="drink">
      <div class="drink__head"><span class="drink__name">Tokyo Iced Tea</span><span class="drink__rule"></span><span class="drink__price">£ 9.50</span></div>
      <p class="drink__mix">Vodka, Gin, Rum, Tequila, Melon Liqueur, Lemon &amp; Lemonade</p>
    </li>
    <li class="drink">
      <div class="drink__head"><span class="drink__name">Tiki Iced Tea</span><span class="drink__rule"></span><span class="drink__price">£ 9.50</span></div>
      <p class="drink__mix">Vodka, Gin, Coconut Rum, Tequila, Orange Liqueur, Lime &amp; Pineapple</p>
    </li>
    <li class="drink">
      <div class="drink__head"><span class="drink__name">Long Island Iced Coffee</span><span class="drink__rule"></span><span class="drink__price">£ 9.50</span></div>
      <p class="drink__mix">Vodka, Gin, Rum, Tequila, Irish Cream, Milk, Salted Caramel Syrup &amp; Espresso</p>
    </li>
  </ul>

  <p class="offer">All £4.95 during<br>Happy Hour</p>

  <div class="footer-mark">MF</div>
  <div class="footer-rule"></div>
</main>
</body>
</html>
```